Kestrel Photography Business Card

I need a business card designed for a photography business based in Perth, Western Australia called Kestrel Photography.

We specialise in wedding, event photography and portrait photography.

The business card must borrow the style of the attached logo.

The hex codes for the colours in the logo are:
#ED1D85 - Pink
#89C23E - Green
#37282F - Black

The name on the card will be:
Name: Toviran
Phone: 0417395268
Website: www.kestrelphotography.com.au
Facebook: kestrelphotography

I am open and happy to accept creative concepts.

I’d like some space at the back for writing notes and appointment details.

```html
<!DOCTYPE html>
<html lang="en">
<head>
<meta charset="utf-8">
<title>Kestrel Photography – Business Card</title>
<link rel="stylesheet" href="https://fonts.googleapis.com/css2?family=Arimo:wght@400;700&display=swap">
<style>
  :root {
    --pink: #ED1D85;
    --green: #89C23E;
    --ink: #37282F;
    --black: #0b0b0b;
    --white: #ffffff;
    --stage: #4a4a4a;
    --paper: #f4f4f4;
    --wordmark-light: #e8e8e8;
    --wordmark-dark: #4a4a4a;
  }
  html, body {
    margin: 0;
    width: 1200px;
    height: 1000px;
    overflow: hidden;
    background: var(--stage);
    font-family: "Arimo", Arial, sans-serif;
  }
  .canvas { position: relative; width: 1200px; height: 1000px; }

  .card { position: absolute; overflow: hidden; }
  .card-front { left: 25px; top: 27px; width: 770px; height: 463px; }
  .card-back { left: 410px; top: 515px; width: 770px; height: 462px; }

  .card-surface { position: absolute; inset: 0; }
  .card-front .card-surface { background: linear-gradient(160deg, #1c1c1c 0%, var(--black) 55%, #151515 100%); }
  .card-back .card-surface { background: linear-gradient(160deg, #ffffff 0%, var(--paper) 50%, #eaeaea 100%); }

  .brand-mark { position: absolute; border-radius: 50%; }
  .card-front .brand-mark { left: 310px; top: 73px; width: 140px; height: 140px; background: var(--white); }
  .card-back .brand-mark { left: 340px; top: 63px; width: 86px; height: 86px; background: var(--pink); }

  .wordmark {
    position: absolute;
    margin: 0;
    font-weight: 400;
    white-space: nowrap;
    text-transform: uppercase;
  }
  .card-front .wordmark {
    left: 83px; top: 254px;
    font-size: 21px; letter-spacing: 0.56em;
    color: var(--wordmark-light);
  }
  .card-back .wordmark {
    left: 200px; top: 168px;
    font-size: 13px; letter-spacing: 0.6em;
    color: var(--wordmark-dark);
  }

  .holder-name {
    position: absolute; left: 82px; top: 351px; margin: 0;
    font-size: 26px; font-weight: 700; color: var(--green);
    text-transform: uppercase;
  }
  .contact-list {
    position: absolute; left: 320px; top: 339px; margin: 0; padding: 0;
    list-style: none; font-size: 18px; line-height: 24px; color: var(--pink);
  }

  .appointment { position: absolute; inset: 0; color: #111; }
  .appointment-title, .notes-title {
    position: absolute; left: 0; width: 770px; margin: 0; text-align: center;
    font-size: 18px; font-weight: 700;
  }
  .appointment-title { top: 213px; left: -30px; }
  .notes-title { top: 324px; left: -30px; }

  .weekdays { position: absolute; top: 252px; left: 0; margin: 0; padding: 0; list-style: none; }
  .weekdays li { position: absolute; font-size: 18px; color: var(--green); white-space: nowrap; }

  .date-row { position: absolute; top: 288px; left: 0; width: 770px; height: 24px; font-size: 18px; }
  .date-row span { position: absolute; top: 0; }
  .date-row .label { font-weight: 700; }
  .write-line { position: absolute; height: 0; border-top: 1.5px solid var(--pink); }
  .notes-line { position: absolute; left: 83px; width: 603px; height: 0; border-top: 1.5px solid var(--green); }
</style>
</head>
<body>
<main class="canvas">

  <section class="card card-front" aria-label="Business card front">
    <div class="card-surface" role="img" aria-label="Black background with a subtle geometric triangle pattern"></div>
    <div class="brand-mark" aria-hidden="true"></div>
    <p class="wordmark">Kestrel Photography</p>
    <p class="holder-name">Toviran</p>
    <ul class="contact-list">
      <li>Phone: 0417395268</li>
      <li>Website: www.kestrelphotography.com.au</li>
      <li>Facebook: kestrelphotography</li>
    </ul>
  </section>

  <section class="card card-back" aria-label="Business card back">
    <div class="card-surface" role="img" aria-label="Light grey background with a subtle geometric triangle pattern"></div>
    <div class="brand-mark" aria-hidden="true"></div>
    <p class="wordmark">Kestrel Photography</p>

    <div class="appointment">
      <h2 class="appointment-title">APPOINTMENT</h2>
      <ul class="weekdays">
        <li style="left:193px">Mon</li>
        <li style="left:267px">Tues</li>
        <li style="left:341px">Wed</li>
        <li style="left:415px">Thurs</li>
        <li style="left:493px">Fri</li>
        <li style="left:548px">Sat</li>
      </ul>
      <div class="date-row">
        <span class="label" style="left:192px">DATE:</span>
        <i class="write-line" style="left:262px; top:15px; width:113px"></i>
        <span style="left:384px">at</span>
        <i class="write-line" style="left:408px; top:15px; width:102px"></i>
        <span class="label" style="left:518px">am/pm</span>
      </div>
      <h2 class="notes-title">NOTES</h2>
      <i class="notes-line" style="top:370px"></i>
      <i class="notes-line" style="top:401px"></i>
    </div>
  </section>

</main>
</body>
</html>
```